Office Building Banner

Need a 4x8 vinyl banner made for our office/storage headquarters. Our branded colors and logo can be taken from our website, www.halvenroofingtx.com. All other elements of our brand have not been decided on yet, so you have creative autonomy there. Our location faces a busy highway in Seguin, Texas, so the banner needs to have our contact information and full name clearly seen from a bit away's away, hope that makes sense. Our company wants to convey attributes of strength, loyalty, protection - basically emulating the qualities of a wolf and his pack. I have uploaded a few items we have been using to date, but as you can see, graphic design is not our forte.

```html
<!DOCTYPE html>
<html lang="en">
<head>
<meta charset="UTF-8">
<title>Halven Roofing &amp; Renovation — Office Banner</title>
<link rel="stylesheet" href="https://fonts.googleapis.com/css2?family=Montserrat:wght@300;700;800;900&display=swap">
<style>
  :root {
    --ink: #0b0b0b;
    --roof-dark: #1c1c1c;
    --roof-mid: #2b2b2b;
    --orange: #ff7a0f;
    --orange-deep: #f26c00;
    --white: #ffffff;
    --page: #ffffff;
  }
  * { box-sizing: border-box; margin: 0; padding: 0; }
  html, body { width: 928px; height: 1200px; overflow: hidden; background: var(--page); }
  body { font-family: "Montserrat", Arial, sans-serif; position: relative; }

  .banner {
    position: absolute;
    left: 40px; top: 388px;
    width: 848px; height: 424px;
    box-shadow: 0 18px 40px rgba(0,0,0,.35);
    overflow: hidden;
  }

  .banner__header {
    position: absolute; left: 0; top: 0;
    width: 100%; height: 226px;
  }
  .roof-texture {
    position: absolute; inset: 0;
    background: linear-gradient(135deg, var(--roof-mid) 0%, var(--roof-dark) 55%, #141414 100%);
  }

  .brand-mark {
    position: absolute; left: 36px; top: 40px;
    width: 180px; height: 150px;
    display: flex; flex-direction: column; align-items: center; justify-content: center; gap: 12px;
  }
  .brand-mark__dot {
    width: 76px; height: 76px; border-radius: 50%;
    background: var(--orange);
  }
  .brand-mark__name {
    font-weight: 800; font-size: 34px; letter-spacing: 1px;
    color: var(--orange);
  }

  .headline {
    position: absolute; left: 222px; top: 40px; right: 28px;
    text-transform: uppercase; line-height: 1;
  }
  .headline__line { display: block; white-space: nowrap; font-weight: 800; }
  .headline__name { color: var(--white); font-size: 55px; letter-spacing: -0.5px; }
  .headline__service { color: var(--orange); font-size: 55px; margin-top: 16px; letter-spacing: -0.5px; }
  .headline__amp { font-weight: 300; margin-right: 10px; }

  .banner__phone {
    position: absolute; left: 0; top: 226px;
    width: 100%; height: 96px;
    background: linear-gradient(90deg, var(--orange) 0%, var(--orange-deep) 100%);
    display: flex; align-items: center; justify-content: center; gap: 22px;
  }
  .phone-icon { width: 62px; height: 62px; flex: none; }
  .phone-number {
    font-weight: 800; font-size: 80px; color: var(--ink);
    letter-spacing: -1px; line-height: 1;
  }

  .banner__web {
    position: absolute; left: 0; top: 322px;
    width: 100%; height: 102px;
    background: var(--white);
    display: flex; align-items: center; justify-content: center;
  }
  .web-address {
    font-weight: 800; font-size: 44px; color: var(--ink); letter-spacing: 0.5px;
  }
  .web-address__name { color: var(--orange); font-weight: 700; }
</style>
</head>
<body>
  <section class="banner">
    <header class="banner__header">
      <div class="roof-texture" role="img" aria-label="Dark close-up of black roof tiles as background texture"></div>
      <div class="brand-mark">
        <span class="brand-mark__dot"></span>
        <span class="brand-mark__name">HALVEN</span>
      </div>
      <h1 class="headline">
        <span class="headline__line headline__name">Halven Roofing</span>
        <span class="headline__line headline__service"><span class="headline__amp">&amp;</span>Renovation</span>
      </h1>
    </header>

    <div class="banner__phone">
      <svg class="phone-icon" viewBox="0 0 62 62" aria-hidden="true">
        <circle cx="31" cy="31" r="31" fill="#0b0b0b"/>
        <path d="M22 16c1.5-1 3-.6 3.8.7l3 5c.7 1.2.4 2.6-.6 3.4l-2 1.6c1.2 3.2 3.7 6 6.8 7.6l1.7-1.9c.9-1 2.3-1.2 3.4-.5l5 3.1c1.3.8 1.6 2.4.7 3.7l-1.8 2.6c-1 1.4-2.8 2-4.4 1.5C28.4 40.6 20.6 32.6 18.3 23.4c-.4-1.6.2-3.3 1.6-4.3z" fill="#fff"/>
        <path d="M34 16a12 12 0 0 1 12 12M34 21a7 7 0 0 1 7 7" fill="none" stroke="#fff" stroke-width="2.6" stroke-linecap="round"/>
      </svg>
      <span class="phone-number">512-555-0148</span>
    </div>

    <div class="banner__web">
      <p class="web-address">www.<span class="web-address__name">halvenroofingtx</span>.com</p>
    </div>
  </section>
</body>
</html>
```